Hot Offer banner for product listing page

Hi, we need a banner in the dimensions 210x390px which will be shown in the product listing on our online shop. There are 18 products and in between randomly there should be 3 banners with three different information.
first banner: fast delivery
The idea is to show a stove which is very "fast". Maybe you can make an effect like in Driftcraft Valorne when they activate the warp drive or something similar. Anyway, the banner should indicate that the delivery is very fast for this product.

second banner: Advantage banner
We would like to have a banner which names all our advantages in our online shop. this is the list of advantages:
- over 200,000 satisfied customers
- Best price guarantee
- thousands of devices in stock
- Top ratings

I attached you some examples, just to give you an idea.

```html
<!DOCTYPE html>
<html lang="en">
<head>
<meta charset="utf-8">
<title>Shop Advantages – Banner Variants</title>
<link rel="stylesheet" href="https://fonts.googleapis.com/css2?family=Exo+2:wght@400&display=swap">
<style>
  :root {
    --page-bg: #ffffff;
    --warm-top: #f28d22;
    --warm-bottom: #d03828;
    --glow-center: #f8b077;
    --glow-edge: #f48226;
    --light-bg: #f8f9fb;
    --badge-center: #f8a866;
    --badge-edge: #f37f21;
    --ink-light: #ffffff;
    --ink-dark: #4a4a50;
  }
  * { box-sizing: border-box; margin: 0; padding: 0; }
  html, body {
    width: 1200px; height: 715px; overflow: hidden;
    background: var(--page-bg);
    font-family: "Exo 2", sans-serif;
  }
  .canvas { position: relative; width: 1200px; height: 715px; }
  .banner {
    position: absolute; top: 39px; width: 345px; height: 641px;
    color: var(--ink-light);
  }
  .banner--warm { left: 42px; background: linear-gradient(180deg, var(--warm-top), var(--warm-bottom)); }
  .banner--glow { left: 424px; background: radial-gradient(ellipse 60% 55% at 50% 52%, var(--glow-center), var(--glow-edge)); }
  .banner--light { left: 830px; background: var(--light-bg); color: var(--ink-dark); }

  .feature { position: absolute; left: 0; width: 100%; text-align: center; }
  .feature--customers { top: 34px; }
  .feature--price { top: 192px; }
  .feature--stock { top: 328px; }
  .feature--ratings { top: 488px; }

  .feature__badge {
    display: block; width: 68px; height: 68px; margin: 0 auto;
    border-radius: 50%; border: 3px solid #fff;
    background: radial-gradient(circle, var(--badge-center), var(--badge-edge) 75%);
  }
  .banner--light .feature__badge { box-shadow: 0 0 3px rgba(0,0,0,0.06); }
  .feature__badge svg { width: 62px; height: 62px; display: block; }
  .feature__label {
    margin-top: 10px; font-size: 20px; line-height: 24px; letter-spacing: 0.3px; font-weight: 400;
  }
  .feature--price .feature__label,
  .feature--ratings .feature__label { margin-top: 14px; }
</style>
</head>
<body>
<svg width="0" height="0" style="position:absolute" aria-hidden="true">
  <defs>
    <g id="icon-headset" fill="none" stroke="#fff" stroke-width="1.5" stroke-linejoin="round">
      <path d="M22 30 v-3 a9 9 0 0 1 18 0 v3"/>
      <rect x="18" y="28" width="5" height="9"/>
      <rect x="39" y="28" width="5" height="9"/>
      <path d="M41 37 q0 5 -5 5 h-3"/>
      <circle cx="31.5" cy="42" r="1.6"/>
    </g>
    <g id="icon-award" fill="none" stroke="#fff" stroke-width="1.5" stroke-linejoin="round">
      <path d="M31 13 l3.5 2.5 4.3-.3 1.6 4 3.6 2.4-1.2 4.1 1.2 4.1-3.6 2.4-1.6 4-4.3-.3-3.5 2.5-3.5-2.5-4.3.3-1.6-4-3.6-2.4 1.2-4.1-1.2-4.1 3.6-2.4 1.6-4 4.3.3z"/>
      <circle cx="31" cy="28.5" r="8"/>
      <path d="M27.5 28.5 l2.5 2.5 4.5-4.5"/>
      <path d="M25 41 v9 l6-3.5 6 3.5 v-9"/>
    </g>
    <g id="icon-stock" fill="none" stroke="#fff" stroke-width="1.5" stroke-linejoin="round">
      <rect x="25" y="16" width="12" height="11"/>
      <path d="M29 16 v3 h4 v-3"/>
      <rect x="20" y="27" width="11" height="11"/>
      <rect x="31" y="27" width="11" height="11"/>
      <path d="M23 27 v3 h3 v-3 M34 27 v3 h3 v-3"/>
      <rect x="14" y="38" width="34" height="5"/>
    </g>
    <path id="star" d="M0 -6 L1.8 -2 L6 -1.9 L2.8 1 L3.7 5.2 L0 3 L-3.7 5.2 L-2.8 1 L-6 -1.9 L-1.8 -2 Z"/>
    <g id="icon-stars" fill="none" stroke="#fff" stroke-width="1.4" stroke-linejoin="round">
      <use href="#star" transform="translate(17 35)"/>
      <use href="#star" transform="translate(31 29)"/>
      <use href="#star" transform="translate(45 35)"/>
    </g>
  </defs>
</svg>

<main class="canvas">
  <section class="banner banner--warm" aria-label="Shop advantages, warm gradient">
    <div class="feature feature--customers"><span class="feature__badge"><svg viewBox="0 0 62 62"><use href="#icon-headset"/></svg></span><p class="feature__label">Over 200,000 Satisfied<br>Customers</p></div>
    <div class="feature feature--price"><span class="feature__badge"><svg viewBox="0 0 62 62"><use href="#icon-award"/></svg></span><p class="feature__label">Best Price Guarantee</p></div>
    <div class="feature feature--stock"><span class="feature__badge"><svg viewBox="0 0 62 62"><use href="#icon-stock"/></svg></span><p class="feature__label">Thousands Of Devices<br>In Stock</p></div>
    <div class="feature feature--ratings"><span class="feature__badge"><svg viewBox="0 0 62 62"><use href="#icon-stars"/></svg></span><p class="feature__label">Top Ratings</p></div>
  </section>

  <section class="banner banner--glow" aria-label="Shop advantages, radial glow">
    <div class="feature feature--customers"><span class="feature__badge"><svg viewBox="0 0 62 62"><use href="#icon-headset"/></svg></span><p class="feature__label">Over 200,000 Satisfied<br>Customers</p></div>
    <div class="feature feature--price"><span class="feature__badge"><svg viewBox="0 0 62 62"><use href="#icon-award"/></svg></span><p class="feature__label">Best Price Guarantee</p></div>
    <div class="feature feature--stock"><span class="feature__badge"><svg viewBox="0 0 62 62"><use href="#icon-stock"/></svg></span><p class="feature__label">Thousands Of Devices<br>In Stock</p></div>
    <div class="feature feature--ratings"><span class="feature__badge"><svg viewBox="0 0 62 62"><use href="#icon-stars"/></svg></span><p class="feature__label">Top Ratings</p></div>
  </section>

  <section class="banner banner--light" aria-label="Shop advantages, light background">
    <div class="feature feature--customers"><span class="feature__badge"><svg viewBox="0 0 62 62"><use href="#icon-headset"/></svg></span><p class="feature__label">Over 200,000 Satisfied<br>Customers</p></div>
    <div class="feature feature--price"><span class="feature__badge"><svg viewBox="0 0 62 62"><use href="#icon-award"/></svg></span><p class="feature__label">Best Price Guarantee</p></div>
    <div class="feature feature--stock"><span class="feature__badge"><svg viewBox="0 0 62 62"><use href="#icon-stock"/></svg></span><p class="feature__label">Thousands Of Devices<br>In Stock</p></div>
    <div class="feature feature--ratings"><span class="feature__badge"><svg viewBox="0 0 62 62"><use href="#icon-stars"/></svg></span><p class="feature__label">Top Ratings</p></div>
  </section>
</main>
</body>
</html>
```